New Trade Show Booth Design Project

We are a security system integrator. Please visit www.qorlinetek.com for info. we would like a simple design that might or might not includes our logo (attached) and a background image. Not sure what that image will be, but it has to project what we do. Maybe a single surveillance camera (attached). The tag line should be " QRL Telemetry - Security Systems Integration"

Target Market(s)

Municipalities, schools, police departments

Font styles to use
Serif
Sans Serif

Requirements
Nice to have
• Bullet points:
Design
Installation
Service
Support

```html
<!DOCTYPE html>
<html lang="en">
<head>
<meta charset="utf-8">
<title>QRL Telemetry - Security Systems Integration</title>
<link rel="stylesheet" href="https://fonts.googleapis.com/css2?family=Archivo+Black&family=Encode+Sans+Condensed:wght@500&family=Oswald:wght@600&display=swap">
<style>
  :root {
    --navy: #0f1d45;
    --navy-mid: #1b3766;
    --red: #c61f26;
    --white: #ffffff;
    --photo-light: #dfe3ee;
    --photo-mid: #a9b2c8;
    --lens-dark: #3a1522;
  }
  * { margin: 0; padding: 0; box-sizing: border-box; }
  html, body { width: 1200px; height: 973px; overflow: hidden; background: #e9e9ec; }
  .booth { position: relative; width: 1200px; height: 973px; overflow: hidden; background: var(--white); }
  .backdrop { position: absolute; inset: 0; }

  .brand { position: absolute; left: 157px; top: 101px; display: flex; align-items: flex-start; gap: 10px; }
  .brand-mark { width: 87px; height: 127px; border: 2px solid var(--navy); border-radius: 50%; flex: none; }
  .brand-name { font-family: "Archivo Black", sans-serif; color: var(--navy); line-height: 1; padding-top: 2px; }
  .brand-name .line-1 { display: block; font-size: 54px; line-height: 50px; }
  .brand-name .line-2 { display: block; font-size: 44px; line-height: 42px; letter-spacing: -0.5px; }
  .brand-tagline { font-family: "Encode Sans Condensed", sans-serif; font-weight: 500; color: var(--red); font-size: 16px; margin-top: 8px; white-space: nowrap; }

  .headline { position: absolute; left: 154px; top: 300px; width: 470px; color: var(--white); font-weight: normal; }
  .headline-main { display: inline-block; font-family: "Oswald", sans-serif; font-weight: 600; font-size: 68px; line-height: 1; letter-spacing: -0.5px; white-space: nowrap; transform: scaleX(0.85); transform-origin: left center; }
  .headline-sub { display: inline-block; font-family: "Archivo Black", sans-serif; font-size: 36px; line-height: 1; letter-spacing: 19.5px; margin-top: 6px; white-space: nowrap; }

  .service-icon { position: absolute; width: 82px; height: 86px; border-radius: 50%; background: var(--white); border: 4px solid var(--red); box-shadow: 0 0 0 3px var(--navy); display: flex; align-items: center; justify-content: center; }
  .service-icon svg { width: 46px; height: 46px; }
  .service-label { position: absolute; height: 39px; color: var(--white); font-family: "Archivo Black", sans-serif; font-size: 23px; display: flex; align-items: center; justify-content: center; }
  .service-label::before { content: ""; position: absolute; inset: 0; background: var(--red); transform: skewX(-18deg); border-bottom: 3px solid var(--white); z-index: 0; }
  .service-label span { position: relative; z-index: 1; }

  .consult-pill { position: absolute; left: 185px; top: 751px; width: 828px; height: 72px; background: var(--white); border-radius: 36px; }
  .consult-text, .phone-number { position: absolute; top: 751px; height: 72px; line-height: 72px; font-family: "Oswald", sans-serif; font-weight: 600; font-size: 56px; white-space: nowrap; transform: scaleX(0.8); transform-origin: left center; }
  .consult-text { left: 226px; color: var(--navy); }
  .phone-number { left: 700px; color: var(--red); }
  .phone-badge { position: absolute; left: 608px; top: 743px; width: 82px; height: 87px; border-radius: 50%; background: var(--white); border: 5px solid var(--red); display: flex; align-items: center; justify-content: center; }
  .phone-badge svg { width: 42px; height: 42px; }

  .web-address { position: absolute; left: 186px; top: 840px; font-family: "Archivo Black", sans-serif; font-size: 32px; letter-spacing: 9px; color: var(--white); white-space: nowrap; }
</style>
</head>
<body>
<main class="booth">
  <svg class="backdrop" width="1200" height="973" viewBox="0 0 1200 973">
    <defs>
      <radialGradient id="camera-photo-tone" cx="0.45" cy="0.4" r="0.7">
        <stop offset="0" stop-color="#f4f5f9"/>
        <stop offset="0.55" stop-color="var(--photo-light)"/>
        <stop offset="1" stop-color="var(--photo-mid)"/>
      </radialGradient>
      <radialGradient id="lens-photo-tone" cx="0.4" cy="0.55" r="0.6">
        <stop offset="0" stop-color="#e0313a"/>
        <stop offset="0.35" stop-color="#6a1f2e"/>
        <stop offset="1" stop-color="var(--lens-dark)"/>
      </radialGradient>
      <linearGradient id="navy-field" x1="0" y1="0" x2="0" y2="1">
        <stop offset="0" stop-color="#0a1638"/>
        <stop offset="1" stop-color="var(--navy-mid)"/>
      </linearGradient>
    </defs>
    <path class="navy-field" d="M0,165 C180,255 430,300 660,272 L1200,230 L1200,973 L0,973 Z" fill="url(#navy-field)"/>
    <path class="red-band" d="M0,826 C330,790 700,796 934,836 C880,885 840,930 798,973 L0,973 Z" fill="var(--red)"/>
    <path d="M0,818 C330,782 700,788 940,828" fill="none" stroke="#ffffff" stroke-opacity="0.6" stroke-width="1.5"/>
    <ellipse cx="960" cy="320" rx="320" ry="400" fill="url(#camera-photo-tone)" stroke="#ffffff" stroke-width="3" role="img" aria-label="Photo of a white dome surveillance camera mounted on a wall bracket"/>
    <ellipse cx="703" cy="594" rx="149" ry="159" fill="url(#lens-photo-tone)" stroke="#ffffff" stroke-width="3" role="img" aria-label="Close-up photo of a dark security camera with a glowing red lens"/>
  </svg>

  <header class="brand">
    <div class="brand-mark"></div>
    <div>
      <div class="brand-name"><span class="line-1">QRL</span><span class="line-2">TELEMETRY</span></div>
      <p class="brand-tagline">Security System Design ★ Installation ★ Service ★ Support</p>
    </div>
  </header>

  <h1 class="headline">
    <span class="headline-main">SECURITY SYSTEMS</span><br>
    <span class="headline-sub">INTEGRATION</span>
  </h1>

  <div class="service-icon" style="left:217px;top:440px;">
    <svg viewBox="0 0 48 48" fill="none" stroke="#c61f26" stroke-width="2.5" stroke-linecap="round"><path d="M8 8 L40 40"/><path d="M40 8 L8 40"/><path d="M36 6 L42 12"/><path d="M10 44 L6 42 L4 38"/></svg>
  </div>
  <div class="service-icon" style="left:399px;top:440px;">
    <svg viewBox="0 0 48 48" fill="none" stroke="#c61f26" stroke-width="2.5"><rect x="6" y="4" width="20" height="38"/><path d="M10 10h12M10 16h12"/><circle cx="32" cy="30" r="8"/><circle cx="32" cy="30" r="3"/></svg>
  </div>
  <div class="service-icon" style="left:217px;top:590px;">
    <svg viewBox="0 0 48 48" fill="none" stroke="#c61f26" stroke-width="2.5" stroke-linecap="round"><path d="M10 38 L36 12"/><circle cx="38" cy="10" r="5"/><path d="M12 10 L38 36"/><circle cx="10" cy="38" r="4"/></svg>
  </div>
  <div class="service-icon" style="left:399px;top:590px;">
    <svg viewBox="0 0 48 48" fill="none" stroke="#c61f26" stroke-width="2.5" stroke-linecap="round"><path d="M10 24 C10 10 38 10 38 24"/><rect x="7" y="22" width="6" height="10" rx="2"/><rect x="35" y="22" width="6" height="10" rx="2"/><path d="M38 32 C38 38 32 40 26 40"/><path d="M10 46 C12 38 36 38 38 46"/></svg>
  </div>

  <div class="service-label" style="left:183px;top:536px;width:150px;"><span>Design</span></div>
  <div class="service-label" style="left:340px;top:536px;width:202px;"><span>Installation</span></div>
  <div class="service-label" style="left:183px;top:687px;width:150px;"><span>Service</span></div>
  <div class="service-label" style="left:340px;top:687px;width:202px;"><span>Support</span></div>

  <div class="consult-pill"></div>
  <p class="consult-text">FREE CONSULTATION</p>
  <div class="phone-badge">
    <svg viewBox="0 0 24 24"><path fill="#c61f26" d="M6.6 10.8c1.4 2.8 3.8 5.1 6.6 6.6l2.2-2.2c.3-.3.7-.4 1-.2 1.1.4 2.3.6 3.6.6.6 0 1 .4 1 1V20c0 .6-.4 1-1 1C10.6 21 3 13.4 3 4c0-.6.4-1 1-1h3.5c.6 0 1 .4 1 1 0 1.3.2 2.5.6 3.6.1.3 0 .7-.2 1z"/></svg>
  </div>
  <p class="phone-number">1.800.555.0142</p>

  <p class="web-address">www.qorlinetek.com</p>
</main>
</body>
</html>
```